Brightwater Medical business cards

Double sided business cards.

Medical technology consulting company.

Business cards with two names on the front, upper to middle left:

Dr Colin R. Haskell MBBS MPH +61491578204
Dr Paul Brennagh PhD MBusLaw +61472019847

Email and website addresses bottom right:

colin@brightwatermedical.com.au
www.brightwatermedical.com.au

Tree logo (as per attached file) on front in a suitable position.

Tag line (as per attached files) on the back.

Need a file format to upload to Desk Ford or Cardmoor.

```html
<!DOCTYPE html>
<html lang="en">
<head>
<meta charset="utf-8">
<title>Brightwater Medical business cards</title>
<link href="https://fonts.googleapis.com/css2?family=Lato:wght@400;700&display=swap" rel="stylesheet">
<style>
  :root {
    --green: #4f9a47;
    --maroon: #6a1417;
    --paper: #ffffff;
    --backdrop: #e9e6e1;
    --shadow: rgba(40, 30, 20, 0.22);
  }
  * { margin: 0; padding: 0; box-sizing: border-box; }
  html, body { width: 1200px; height: 800px; overflow: hidden; }
  body {
    background: var(--backdrop);
    font-family: "Lato", sans-serif;
    position: relative;
  }
  .card {
    position: absolute;
    width: 540px;
    height: 309px;
    background: var(--paper);
    box-shadow: 0 8px 24px var(--shadow);
    overflow: hidden;
  }
  .card--back { left: 60px; top: 100px; }
  .card--front { left: 600px; top: 390px; }

  .brand {
    display: flex;
    align-items: center;
    gap: 10px;
  }
  .brand-dot {
    width: 30px; height: 30px;
    border-radius: 50%;
    background: var(--green);
    flex: none;
  }
  .brand-name {
    font-weight: 400;
    color: var(--green);
    letter-spacing: 0.04em;
    text-transform: uppercase;
    white-space: nowrap;
  }

  .card--back .brand {
    position: absolute;
    left: 0; right: 0; top: 118px;
    justify-content: center;
  }
  .card--back .brand-dot { width: 42px; height: 42px; }
  .card--back .brand-name { font-size: 34px; }
  .tagline {
    position: absolute;
    left: 0; right: 0; top: 176px;
    text-align: center;
    color: var(--green);
    font-size: 19px;
    letter-spacing: 0.02em;
  }
  .tagline .divider { color: var(--maroon); margin: 0 6px; }

  .people {
    position: absolute;
    left: 26px; top: 34px;
  }
  .person + .person { margin-top: 16px; }
  .person-name {
    color: var(--maroon);
    font-weight: 700;
    font-size: 15px;
  }
  .person-credentials {
    color: var(--green);
    font-weight: 400;
    font-size: 10px;
    margin-left: 3px;
  }
  .contact-line {
    display: flex;
    align-items: center;
    gap: 8px;
    margin-top: 5px;
    color: var(--green);
    font-size: 12.5px;
  }
  .contact-icon { width: 14px; height: 14px; flex: none; }

  .card--front .brand {
    position: absolute;
    left: 140px; top: 150px;
  }
  .card--front .brand-name { font-size: 22px; }

  .web-contacts {
    position: absolute;
    right: 22px; top: 208px;
  }
  .web-contacts .contact-line { font-size: 11px; margin-top: 6px; }

  .edge-band {
    position: absolute;
    left: 0; right: 0; bottom: 0;
  }
  .edge-band__green { height: 5px; background: var(--green); }
  .edge-band__gap { height: 3px; background: var(--paper); }
  .edge-band__maroon { height: 9px; background: var(--maroon); }
</style>
</head>
<body>

  <section class="card card--back" aria-label="Card back">
    <div class="brand">
      <span class="brand-dot"></span>
      <span class="brand-name">Brightwater Medical</span>
    </div>
    <p class="tagline">Research<span class="divider">|</span>Development<span class="divider">|</span>Market</p>
  </section>

  <section class="card card--front" aria-label="Card front">
    <div class="people">
      <div class="person">
        <p class="person-name">Dr Colin R. Haskell<span class="person-credentials">MBBS MPH</span></p>
        <p class="contact-line">
          <svg class="contact-icon" viewBox="0 0 16 16" aria-hidden="true">
            <circle cx="8" cy="8" r="7" fill="none" stroke="#6a1417" stroke-width="1.2"/>
            <path d="M5.3 4.6l1.3-.3.7 1.7-.9.6c.4.9 1.1 1.6 2 2l.6-.9 1.7.7-.3 1.3c-2.7.1-5.2-2.4-5.1-5.1z" fill="#6a1417"/>
          </svg>
          +61491578204
        </p>
      </div>
      <div class="person">
        <p class="person-name">Dr Paul Brennagh<span class="person-credentials">PhD MBusLaw</span></p>
        <p class="contact-line">
          <svg class="contact-icon" viewBox="0 0 16 16" aria-hidden="true">
            <circle cx="8" cy="8" r="7" fill="none" stroke="#6a1417" stroke-width="1.2"/>
            <path d="M5.3 4.6l1.3-.3.7 1.7-.9.6c.4.9 1.1 1.6 2 2l.6-.9 1.7.7-.3 1.3c-2.7.1-5.2-2.4-5.1-5.1z" fill="#6a1417"/>
          </svg>
          +61472019847
        </p>
      </div>
    </div>

    <div class="brand">
      <span class="brand-dot"></span>
      <span class="brand-name">Brightwater Medical</span>
    </div>

    <div class="web-contacts">
      <p class="contact-line">
        <svg class="contact-icon" viewBox="0 0 16 16" aria-hidden="true">
          <circle cx="8" cy="8" r="7" fill="none" stroke="#6a1417" stroke-width="1.2"/>
          <rect x="4.5" y="5.5" width="7" height="5" fill="none" stroke="#6a1417" stroke-width="1"/>
          <path d="M4.5 5.5L8 8.3l3.5-2.8" fill="none" stroke="#6a1417" stroke-width="1"/>
        </svg>
        colin@brightwatermedical.com.au
      </p>
      <p class="contact-line">
        <svg class="contact-icon" viewBox="0 0 16 16" aria-hidden="true">
          <circle cx="8" cy="8" r="7" fill="none" stroke="#6a1417" stroke-width="1.2"/>
          <circle cx="8" cy="8" r="3.6" fill="none" stroke="#6a1417" stroke-width="1"/>
          <path d="M4.4 8h7.2M8 4.4c-1.4 2.2-1.4 5 0 7.2M8 4.4c1.4 2.2 1.4 5 0 7.2" fill="none" stroke="#6a1417" stroke-width="0.8"/>
        </svg>
        www.brightwatermedical.com.au
      </p>
    </div>

    <div class="edge-band" aria-hidden="true">
      <div class="edge-band__green"></div>
      <div class="edge-band__gap"></div>
      <div class="edge-band__maroon"></div>
    </div>
  </section>

</body>
</html>
```